Brackenford Group Website

We have a newly established brand for a company with an existing portfolio of property. The company is corporate and professional and both owns and develops property. The website should reflect a professional and stable organisation. The website should showcase the existing properties (6), have a home page that describes the company and its activities and has a "about us" page. The website will be in Wordpress and we would like the code for all pages to be sent to us by the successful designer upon completion of the job.

sorry was called from the office on an urgent matter. To be fair on submitters, i need a couple more days to finalise reviews.

Contact Information for Business Card

Brackenford Logo on front
Black background with silver logo.

Coding

Number of Pages Required

5+ page

Colors

Designer to choose colors to be used in the design.

Requirements
Must have
• Text side of card should include
• Brackenford Property Group (as title in logo font)
• Employee Name (centered)
• Job Title (centered below name)
• Address 4 lines
• Email, mobile office phone, 3 lines
• website address (probably as footer)

```html
<!DOCTYPE html>
<html lang="en">
<head>
<meta charset="utf-8">
<title>Brackenford Property Group</title>
<link href="https://fonts.googleapis.com/css2?family=Oswald:wght@600&family=Libre+Baskerville:ital,wght@0,400;1,400&family=Montserrat:ital,wght@0,400;0,500;0,600;1,400&display=swap" rel="stylesheet">
<style>
:root{
  --orange:#d4532e;
  --navy:#1d2433;
  --ink:#222;
  --grey:#777;
  --line:#e3e3e3;
  --white:#fff;
}
*{margin:0;padding:0;box-sizing:border-box}
html,body{width:1200px;height:4854px;overflow:hidden;background:var(--white)}
body{position:relative;font-family:"Montserrat",sans-serif;color:var(--ink)}
.abs{position:absolute}
.serif{font-family:"Libre Baskerville",serif}
svg.layer{position:absolute;left:0;top:0}

/* hero */
.nav{position:absolute;top:36px;right:75px;display:flex;gap:24px;font-size:13px;font-weight:500;color:var(--white);letter-spacing:.3px}
.nav .active{color:var(--orange)}
.nav .active::before{content:"";display:inline-block;width:9px;height:9px;border-radius:50%;background:var(--orange);margin-right:6px}
.brand{position:absolute;font-family:"Libre Baskerville",serif;color:var(--white);letter-spacing:1px;text-align:center}
.hero-title{left:77px;top:196px;font-family:"Oswald",sans-serif;font-size:46px;line-height:54px;color:var(--white);text-transform:uppercase}
.hero-sub{left:78px;top:306px;font-size:16px;line-height:26px;color:#e8e8e8;width:375px}
.btn{position:absolute;background:var(--orange);color:var(--white);font-family:"Libre Baskerville",serif;font-size:14px;letter-spacing:.5px;display:flex;align-items:center;justify-content:center;gap:16px}
.dots{position:absolute;left:1156px;top:270px;display:flex;flex-direction:column;gap:13px}
.dots span{width:12px;height:12px;border-radius:50%;border:1.5px solid #ddd}
.dots span.on{background:var(--orange);border-color:var(--orange)}

/* about */
.h2{font-family:"Libre Baskerville",serif;font-size:40px;color:var(--ink)}
.about-copy{left:642px;top:806px;width:440px;font-size:12.5px;line-height:27px;color:var(--grey)}
.about-copy p{margin-bottom:14px}
.explore{font-family:"Libre Baskerville",serif;color:var(--orange);font-size:18px}

/* expertise */
.exp-title{left:78px;top:1350px;color:var(--white);font-size:40px}
.acq{left:175px;top:1446px;color:var(--white);font-size:26px}
.acq-copy{left:179px;top:1505px;width:360px;font-size:13.5px;line-height:27px;font-style:italic;color:#fbe2d8}
.services{left:78px;top:1808px;list-style:none}
.services li{font-size:13.5px;color:var(--white);text-decoration:underline;height:43px;display:flex;align-items:flex-start;gap:22px}
.services li::before{content:"";width:10px;height:10px;border-radius:50%;background:var(--white);margin-top:4px}

/* case studies */
.cs-title{left:0;width:1200px;top:2232px;text-align:center}
.card{position:absolute;width:323px;height:321px;border-bottom:2px solid var(--line)}
.card .photo{height:227px}
.card h3{position:absolute;left:2px;top:251px;font-family:"Libre Baskerville",serif;font-size:15px;font-weight:400}
.card p{position:absolute;left:2px;top:280px;font-size:12px;color:var(--grey)}
.card .go{position:absolute;right:0;top:252px;width:42px;height:42px;border-radius:50%;background:var(--orange)}
.card .go svg{position:absolute;left:11px;top:11px}
.card.first::after{content:"";position:absolute;left:0;bottom:-2px;width:62px;height:3px;background:var(--orange)}

/* team */
.team-title{left:79px;top:3385px;color:var(--white);font-size:40px;line-height:49px}
.arrow-dot{position:absolute;width:40px;height:40px;border-radius:50%;background:var(--orange)}
.arrow-dot svg{position:absolute;left:10px;top:10px}
.member{left:700px;width:410px;text-align:center;color:var(--white)}

/* cta */
.cta{left:0;width:1200px;top:4202px;text-align:center;font-size:34px;line-height:52px;color:var(--ink)}

/* footer */
.f-col h4{font-family:"Libre Baskerville",serif;font-weight:400;font-size:16px;color:var(--white);margin-bottom:26px;letter-spacing:.5px}
.f-text{font-size:12px;line-height:27px;color:#c9c9c9}
.f-row{display:flex;gap:20px;margin-bottom:12px}
.input{position:absolute;left:884px;top:4646px;width:239px;height:44px;background:var(--white);font-size:12px;color:#888;padding:14px 14px}
.copyright{left:0;top:4791px;width:1200px;height:63px;background:var(--orange);color:var(--white);font-size:12px;text-align:center;line-height:63px}
</style>
</head>
<body>

<!-- HERO -->
<svg class="layer" width="1200" height="700">
  <defs>
    <linearGradient id="heroGrad" x1="0" y1="0" x2="1" y2="1">
      <stop offset="0" stop-color="#2a2a2e"/><stop offset=".55" stop-color="#3b3330"/><stop offset="1" stop-color="#1f1c1c"/>
    </linearGradient>
    <linearGradient id="hexGrad" x1="0" y1="0" x2="0" y2="1">
      <stop offset="0" stop-color="#b79ac0"/><stop offset=".5" stop-color="#8a4a3a"/><stop offset="1" stop-color="#3a2420"/>
    </linearGradient>
  </defs>
  <polygon points="0,0 1200,0 1200,640 0,555" fill="url(#heroGrad)" role="img" aria-label="City towers seen from street level at dusk"/>
  <line x1="0" y1="555" x2="1200" y2="640" stroke="#d4532e" stroke-width="4"/>
  <polygon points="935,160 1075,290 1075,410 935,540 795,410 795,290" fill="url(#hexGrad)" role="img" aria-label="Hexagonal window on a glass office tower against a lilac sky"/>
</svg>
<div class="brand" style="left:75px;top:42px;font-size:14px">BRACKENFORD</div>
<nav class="nav"><span class="active">HOME</span><span>ABOUT</span><span>EXPERTISE</span><span>CASE STUDIES</span><span>TEAM</span><span>CONTACT US</span></nav>
<svg class="abs" style="left:1106px;top:37px" width="14" height="14" viewBox="0 0 14 14"><circle cx="6" cy="6" r="4.5" fill="none" stroke="#d4532e" stroke-width="2"/><line x1="9.5" y1="9.5" x2="13" y2="13" stroke="#d4532e" stroke-width="2"/></svg>
<h1 class="abs hero-title">Brackenford<br>Property Group</h1>
<p class="abs hero-sub">Expertise in redevelopment and Repurposing to continuously Improve value.</p>
<div class="btn" style="left:77px;top:373px;width:202px;height:49px">CONTACT US
  <svg width="30" height="10" viewBox="0 0 30 10"><path d="M0 5H28M23 1l5 4-5 4" stroke="#fff" stroke-width="1.4" fill="none"/></svg></div>
<div class="dots"><span></span><span></span><span class="on"></span><span></span><span></span></div>

<!-- ABOUT -->
<svg class="abs" style="left:100px;top:670px" width="440" height="550">
  <defs><linearGradient id="brick" x1="0" y1="0" x2="1" y2="1"><stop offset="0" stop-color="#c9663f"/><stop offset=".6" stop-color="#9c3f24"/><stop offset="1" stop-color="#2f3a4a"/></linearGradient>
  <linearGradient id="glass" x1="0" y1="0" x2="1" y2="1"><stop offset="0" stop-color="#e8eef2"/><stop offset="1" stop-color="#5f7f96"/></linearGradient></defs>
  <polygon points="260,70 425,250 340,425 110,425 10,250 115,70" fill="url(#brick)" role="img" aria-label="Brick apartment building rising into a blue sky"/>
  <polygon points="100,5 155,35 155,100 100,130 45,100 45,35" fill="url(#glass)" role="img" aria-label="Balconies on a modern apartment block"/>
  <polygon points="335,340 430,395 430,495 335,545 245,495 245,395" fill="url(#glass)" role="img" aria-label="Curved glass facade of an office building"/>
</svg>
<h2 class="abs h2" style="left:644px;top:742px">ABOUT US</h2>
<div class="abs about-copy">
  <p>Brackenford Group is a privately-owned commercial real estate investment company founded in Auckland in 2007. Working with a small group of long-standing private and institutional partners, the firm has successfully acquired and developed assets valued at over $1.0 billion.</p>
  <p>Brackenford Group has a long track record of success in the acquisition, consenting, development, renovation and repositioning of office, tourism accommodation, residential, social housing, retail and mixed use properties within the Auckland region.</p>
  <p>Drawing upon the decades of experience of its principals, partners and the skill sets of the Brackenford team, the company has been able to identify many successful real estate</p>
</div>
<div class="abs explore" style="left:646px;top:1182px">Explore More <span style="font-size:12px">&#9654;</span></div>

<!-- EXPERTISE -->
<svg class="layer" style="top:1280px" width="1200" height="910">
  <defs><linearGradient id="meet" x1="0" y1="0" x2="1" y2="1"><stop offset="0" stop-color="#6c6d70"/><stop offset=".6" stop-color="#3e4043"/><stop offset="1" stop-color="#2d2e30"/></linearGradient></defs>
  <polygon points="0,10 765,10 640,896 0,790" fill="#d4532e"/>
  <polygon points="656,90 1200,90 1200,727 560,727" fill="url(#meet)" role="img" aria-label="Overhead view of business people shaking hands across a glass table"/>
</svg>
<h2 class="abs serif exp-title" style="font-weight:400">EXPERTISE</h2>
<div class="abs" style="left:0;top:1463px;width:78px;height:2px;background:#fff"></div>
<svg class="abs" style="left:74px;top:1424px" width="78" height="84"><polygon points="39,2 74,22 74,62 39,82 4,62 4,22" fill="#fff"/><path d="M24 44l9-8 8 4 7-5 8 9-12 8z" fill="#222"/></svg>
<h3 class="abs serif acq" style="font-weight:400">ACQUISITIONS</h3>
<p class="abs acq-copy">Prior to any successful real estate acquisition we plan and implement proactive and thoughtful market and asset research. The Brackenford team prides itself on our ability to evaluate market opportunities before others see them. We use our longstanding relationships with the brokerage and broader real estate community together with our reputation for “delivering on our promises” to purchase and position unique investment opportunities.</p>
<ul class="abs services">
  <li>RESOURCE MANAGEMENT PLANNING &amp; CONSENTING</li>
  <li>DEVELOPMENT</li>
  <li>RENOVATION AND REPOSITIONING</li>
  <li>LEASING AND ASSET MANAGEMENT</li>
  <li>FINANCIAL MANAGEMENT</li>
</ul>

<!-- CASE STUDIES -->
<h2 class="abs h2 cs-title">CASE STUDIES</h2>
<div class="card first" style="left:77px;top:2323px"><div class="photo" style="background:linear-gradient(180deg,#3b4a7a,#c7866a 55%,#1f3d8a)" role="img" aria-label="City skyline across the harbour at dusk"></div><h3>ALDERWICK</h3><p>Alderwick, 41 Tamar Ave, Auckland CBD</p><div class="go"><svg width="20" height="20"><path d="M2 10h15M12 5l5 5-5 5" stroke="#fff" stroke-width="1.6" fill="none"/></svg></div></div>
<div class="card" style="left:439px;top:2323px"><div class="photo" style="background:linear-gradient(90deg,#b4725a,#2bb3e6 40%,#2bb3e6 60%,#a86b55)" role="img" aria-label="Two brick towers framing a bright blue sky"></div><h3>THE HALLOWAY</h3><p>Brackenford Property Group</p><div class="go"><svg width="20" height="20"><path d="M2 10h15M12 5l5 5-5 5" stroke="#fff" stroke-width="1.6" fill="none"/></svg></div></div>
<div class="card" style="left:801px;top:2323px"><div class="photo" style="background:linear-gradient(135deg,#3a8a8f,#1c5a66 60%,#e9eef0)" role="img" aria-label="Curved teal glass tower"></div><h3>MERRIDALE</h3><p>Brackenford Property Group</p><div class="go"><svg width="20" height="20"><path d="M2 10h15M12 5l5 5-5 5" stroke="#fff" stroke-width="1.6" fill="none"/></svg></div></div>
<div class="card" style="left:77px;top:2698px"><div class="photo" style="background:linear-gradient(90deg,#d6d8da,#9a5a3e 45%,#e4e6e8 70%,#4a5258)" role="img" aria-label="Modern apartment blocks with brick and glass facades"></div><h3>CASTLETON</h3><p>Brackenford Property Group</p><div class="go"><svg width="20" height="20"><path d="M2 10h15M12 5l5 5-5 5" stroke="#fff" stroke-width="1.6" fill="none"/></svg></div></div>
<div class="card" style="left:439px;top:2698px"><div class="photo" style="background:linear-gradient(180deg,#6f93a8,#bfcad2 50%,#e7e2dc)" role="img" aria-label="White apartment building with red balconies"></div><h3>WESTBRIDGE</h3><p>Brackenford Property Group</p><div class="go"><svg width="20" height="20"><path d="M2 10h15M12 5l5 5-5 5" stroke="#fff" stroke-width="1.6" fill="none"/></svg></div></div>
<div class="card" style="left:801px;top:2698px"><div class="photo" style="background:linear-gradient(90deg,#b48a6a,#5a3a2e 50%,#8a5a44)" role="img" aria-label="Brick warehouse buildings with a rooftop water tower"></div><h3>SIX TWENTY</h3><p>Brackenford Property Group</p><div class="go"><svg width="20" height="20"><path d="M2 10h15M12 5l5 5-5 5" stroke="#fff" stroke-width="1.6" fill="none"/></svg></div></div>

<!-- TEAM -->
<svg class="layer" style="top:3080px" width="1200" height="900">
  <defs><linearGradient id="night" x1="0" y1="0" x2="0" y2="1"><stop offset="0" stop-color="#1a2238"/><stop offset="1" stop-color="#2a2a35"/></linearGradient>
  <linearGradient id="portrait" x1="0" y1="0" x2="0" y2="1"><stop offset="0" stop-color="#8a8f96"/><stop offset="1" stop-color="#4a4e55"/></linearGradient></defs>
  <polygon points="433,6 1200,6 1200,763 584,891" fill="#d4532e"/>
  <polygon points="0,89 528,89 640,722 0,722" fill="url(#night)" role="img" aria-label="City skyline at night"/>
  <rect x="754" y="70" width="263" height="426" fill="url(#portrait)" role="img" aria-label="Portrait of a team member in a grey suit"/>
</svg>
<h2 class="abs serif team-title" style="font-weight:400">MEET THE<br>TEAM</h2>
<div class="arrow-dot" style="left:80px;top:3512px"><svg width="20" height="20"><path d="M18 10H3M8 5l-5 5 5 5" stroke="#fff" stroke-width="1.6" fill="none"/></svg></div>
<div class="arrow-dot" style="left:127px;top:3512px"><svg width="20" height="20"><path d="M2 10h15M12 5l5 5-5 5" stroke="#fff" stroke-width="1.6" fill="none"/></svg></div>
<div class="abs member serif" style="top:3616px;font-size:19px">MARCUS HALE</div>
<div class="abs member" style="top:3652px;font-size:12px;font-style:italic;font-weight:600">Senior Asset and Development Manager</div>
<div class="abs member" style="top:3708px;font-size:13px;line-height:26px">20-30 word summary A leading<br>manager in the xxxxxxxx</div>
<div class="abs" style="left:884px;top:3785px;width:40px;height:40px;border-radius:50%;background:#1e88d2" role="img" aria-label="Professional profile link"></div>

<!-- CTA -->
<div class="abs" style="left:546px;top:4052px;width:110px;height:110px;border-radius:50%;background:linear-gradient(135deg,#2e3450,#c4673e)" role="img" aria-label="Brand emblem"></div>
<h2 class="abs serif cta" style="font-weight:400">The Best Property Group<br>Start with the BRACKENFORD</h2>
<div class="btn" style="left:497px;top:4314px;width:204px;height:49px">CONTACT US
  <svg width="30" height="10" viewBox="0 0 30 10"><path d="M0 5H28M23 1l5 4-5 4" stroke="#fff" stroke-width="1.4" fill="none"/></svg></div>

<!-- FOOTER -->
<svg class="layer" style="top:4350px" width="1200" height="504">
  <polygon points="0,13 1200,168 1200,504 0,504" fill="#1c1e24"/>
  <line x1="0" y1="13" x2="1200" y2="168" stroke="#d4532e" stroke-width="4"/>
  <circle cx="130" cy="36" r="20" fill="#d4532e"/>
  <path d="M130 46V27M124 33l6-6 6 6" stroke="#fff" stroke-width="1.6" fill="none"/>
</svg>
<div class="brand" style="left:77px;top:4540px;font-size:15px">BRACKENFORD</div>
<div class="abs f-text" style="left:78px;top:4590px;width:230px">Brackenford Group is a privately -owned commercial real estate investment company founded in Auckland in 2007.</div>
<div class="abs explore" style="left:79px;top:4714px;font-size:17px">Explore More <span style="font-size:11px">&#9654;</span></div>

<div class="abs f-col" style="left:348px;top:4536px">
  <h4>CONTACT US</h4>
  <div class="f-row"><svg width="16" height="22"><path d="M8 21C3 13 1 10 1 7a7 7 0 0114 0c0 3-2 6-7 14z" fill="#d4532e"/><circle cx="8" cy="7" r="2.5" fill="#1c1e24"/></svg>
    <div class="f-text">Brackenford Group Ltd<br>Level 4, Kestrel Court<br>12 Kestrel Lane<br>Auckland CBD</div></div>
  <div class="f-row"><svg width="16" height="22"><path d="M8 21C3 13 1 10 1 7a7 7 0 0114 0c0 3-2 6-7 14z" fill="#d4532e"/><circle cx="8" cy="7" r="2.5" fill="#1c1e24"/></svg>
    <div class="f-text">PO Box 2208 Wexford St<br>Auckland 1140</div></div>
</div>

<div class="abs f-col" style="left:616px;top:4536px">
  <h4>CONTACT INFO</h4>
  <div class="f-row" style="gap:16px;margin-bottom:2px"><svg width="18" height="18"><path d="M3 1l4 0 2 5-3 2c1 2 3 4 5 5l2-3 5 2v4c0 1-1 2-2 2C8 18 0 10 1 3c0-1 1-2 2-2z" fill="#d4532e"/></svg><span class="f-text">+64 9 555 0148</span></div>
  <div class="f-row" style="gap:16px"><svg width="18" height="18"><rect x="1" y="4" width="16" height="11" fill="#d4532e"/><path d="M1 4l8 6 8-6" stroke="#1c1e24" stroke-width="1.3" fill="none"/></svg><span class="f-text">marcus@brackenfordgroup.co.nz</span></div>
  <div style="display:flex;gap:8px;margin-top:6px">
    <div style="width:38px;height:38px;border-radius:50%;background:#3b5998" role="img" aria-label="Social link"></div>
    <div style="width:38px;height:38px;border-radius:50%;background:#1da1f2" role="img" aria-label="Social link"></div>
    <div style="width:38px;height:38px;border-radius:50%;background:#1e88d2" role="img" aria-label="Social link"></div>
  </div>
</div>

<div class="abs f-col" style="left:885px;top:4536px;width:240px">
  <h4>NEWSLETTER</h4>
  <div class="f-text">Would you like to receive our exclusive update for sign up !</div>
</div>
<div class="input">Enter Email *</div>
<div class="btn" style="left:884px;top:4698px;width:239px;height:44px;font-size:13px">SUBSCRIBE
  <svg width="30" height="10" viewBox="0 0 30 10"><path d="M0 5H28M23 1l5 4-5 4" stroke="#fff" stroke-width="1.4" fill="none"/></svg></div>

<div class="abs copyright">©BRACKENFORD PROPERTY GROUP - 2019 All Rights Reserved.</div>

</body>
</html>
```